GDFH Business Card

Looking for a business card design to incorporate our branding. We want to only use the colors listing in the Branding Package (attached).
Updates

Target Market(s)

People who need their phone or device fixed.

Industry/Entity Type

Electronics

Contact Information for Business Card

Please use:

Gadget Fix Haven LLC
4870 S Ridgecrest Pkwy
Suite 318
San Antonio, TX 78291

Wendell Thorsby, Store Manager

(210) 555-0147

Requirements
Must have
• Must include the colors that are contained within the Branding Package PDF file.

```html
<!DOCTYPE html>
<html lang="en">
<head>
<meta charset="utf-8">
<title>Gadget Fix Haven – Business Card</title>
<link rel="stylesheet" href="https://fonts.googleapis.com/css2?family=Arimo:wght@400&display=swap">
<style>
  :root {
    --stage: #111111;
    --lime: #d3da5a;
    --lime-dark: #c4cb4a;
    --orange: #f15a24;
    --white: #ffffff;
    --ink: #555555;
  }
  * { margin: 0; padding: 0; box-sizing: border-box; }
  html, body {
    width: 1200px; height: 1000px; overflow: hidden;
    background: var(--stage);
    font-family: "Arimo", Arial, sans-serif;
  }
  .card {
    position: absolute;
    width: 520px; height: 310px;
    border-radius: 22px;
    overflow: hidden;
  }
  .card--back {
    left: 50px; top: 170px;
    background: linear-gradient(135deg, #dde36e 0%, var(--lime) 55%, var(--lime-dark) 100%);
    display: flex; align-items: center; justify-content: center;
  }
  .card--front {
    left: 630px; top: 480px;
    background: var(--white);
  }
  .brand {
    display: flex; align-items: center; gap: 10px;
    color: var(--orange);
    font-size: 28px; font-weight: 400;
    white-space: nowrap;
  }
  .brand__mark {
    width: 34px; height: 34px; border-radius: 7px;
    background: var(--orange);
  }
  .card--front .brand {
    position: absolute; right: 34px; top: 44px;
    font-size: 24px;
  }
  .card--front .brand__mark { width: 30px; height: 30px; }
  .person {
    position: absolute; left: 34px; top: 52px;
  }
  .person__name { color: var(--orange); font-size: 20px; line-height: 1.1; }
  .person__role { color: var(--ink); font-size: 15px; line-height: 1.2; }
  .contacts {
    position: absolute; left: 34px; top: 116px;
    list-style: none; color: var(--ink); font-size: 14px; line-height: 20px;
  }
  .contacts li { display: flex; align-items: center; gap: 8px; }
  .contacts svg { width: 12px; height: 12px; fill: var(--orange); flex: none; }
  .address {
    position: absolute; right: 34px; bottom: 58px;
    text-align: right; color: var(--ink); font-size: 17px; line-height: 22px;
    font-style: normal;
  }
  .band {
    position: absolute; left: 0; right: 0; bottom: 0; height: 40px;
    background: var(--lime);
  }
  .band__accent {
    position: absolute; right: 0; bottom: 0; width: 250px; height: 40px;
    background: var(--orange);
    border-top-left-radius: 24px;
  }
</style>
</head>
<body>
  <section class="card card--back" aria-label="Card back">
    <div class="brand"><span class="brand__mark"></span>Gadget Fix Haven</div>
  </section>

  <section class="card card--front" aria-label="Card front">
    <div class="person">
      <p class="person__name">Wendell Thorsby</p>
      <p class="person__role">Store Manager</p>
    </div>
    <ul class="contacts">
      <li><svg viewBox="0 0 24 24"><path d="M6.6 10.8a15 15 0 0 0 6.6 6.6l2.2-2.2a1 1 0 0 1 1-.25 11.4 11.4 0 0 0 3.6.57 1 1 0 0 1 1 1V20a1 1 0 0 1-1 1A17 17 0 0 1 3 4a1 1 0 0 1 1-1h3.5a1 1 0 0 1 1 1c0 1.25.2 2.45.57 3.57a1 1 0 0 1-.25 1z"/></svg>(210) 555-0147</li>
      <li><svg viewBox="0 0 24 24"><path d="M2 5h20v14H2z M2 5l10 8 10-8" /></svg>hello@gadgetfixhaven.com</li>
      <li><svg viewBox="0 0 24 24"><circle cx="12" cy="12" r="10"/></svg>www.gadgetfixhaven.com</li>
    </ul>
    <div class="brand"><span class="brand__mark"></span>Gadget Fix Haven</div>
    <address class="address">
      4870 S Ridgecrest Pkwy<br>
      Suite 318<br>
      San Antonio, TX 78291
    </address>
    <div class="band"></div>
    <div class="band__accent"></div>
  </section>
</body>
</html>
```